Business card for dental office with laser therapy / dental facial esthetic

A simple logo which should signifies
Dentistry intraoral as primary and with extended extraoral cosmetic facial esthetic services ( regenerative skincare ) which enhance Beauty as whole .
Conservative high tech approach by using laser intraoral and extraoral limited to face and neck
Front Face :May be black background with neon blue / purplish Rim signifies laser ( ?) & abstract face profile and tooth or Apple design in one ? / see upload inspiration design
Back side : simple appointment slots with date and time / white background / black letter

Color : black/ neon blue/ purplish and gold incorporate for logo design
Final design : dental / esthetic / modern high tech and safe

Target Market(s)

Dental Patients who seeks more high end cosmetic treatment

Industry/Entity Type

Health Care

Contact Information for Business Card

Esthetic modern elegant looking
Logo and office must haves important informations

Logo Text

Family & Cosmetic Dentistry

Font styles to use
Script

Requirements
Must have
• Name of practice and all important informations
• Family & Cosmetic Dentistry
• Lan B. Okafor DMD,PC
• 38412 Brantley Court ,ste.207
• Cedar Hollow ,VA 20391
• Ph. 703-555-0187
• Fax 703-5550193
Nice to have
• More abstract
• Front : black back ground with neon blue rim (signifies laser therapy)
• Logo can also be golden gold / neon blue
• Address & Infos can be white
Should not have
• Not to busy looking

```html
<!DOCTYPE html>
<html lang="en">
<head>
<meta charset="utf-8">
<title>Lumen Family &amp; Cosmetic Dentistry – Business Card</title>
<link rel="stylesheet" href="https://fonts.googleapis.com/css2?family=Montserrat:wght@600;700&family=Roboto:wght@400;500;700&display=swap">
<style>
  :root {
    --stage: #ecebe8;
    --card-white: #ffffff;
    --card-black: #0b0b0d;
    --ink: #1a1a1a;
    --dot-line: #555555;
    --watermark: #e3e3e3;
    --gold: #d9ad3c;
    --neon-blue: #7fd3ff;
    --cyan: #35c7e6;
    --purple: #6a3fc7;
  }
  * { box-sizing: border-box; margin: 0; padding: 0; }
  html, body { width: 1200px; height: 800px; overflow: hidden; }
  body {
    background: var(--stage);
    display: flex;
    align-items: center;
    justify-content: center;
    gap: 48px;
  }
  .card {
    position: relative;
    width: 540px;
    height: 309px;
    border-radius: 4px;
    overflow: hidden;
    box-shadow: 0 10px 28px rgba(0,0,0,0.18);
  }

  /* Back: appointment side */
  .card-back {
    background: var(--card-white);
    font-family: "Montserrat", sans-serif;
    color: var(--ink);
  }
  .card-back .faint-mark {
    position: absolute;
    left: 150px; top: 40px;
    width: 230px; height: 230px;
    border-radius: 50%;
    background: var(--watermark);
    opacity: 0.55;
  }
  .appointment-title {
    position: absolute;
    top: 52px; left: 0; right: 0;
    text-align: center;
    font-size: 12px;
    font-weight: 700;
    letter-spacing: 2.5px;
  }
  .slots {
    position: absolute;
    left: 40px; right: 40px; top: 86px;
    display: grid;
    grid-template-columns: 1fr 1fr;
    row-gap: 26px;
    column-gap: 28px;
  }
  .slot {
    display: flex;
    align-items: flex-end;
    font-size: 11px;
    font-weight: 700;
    letter-spacing: 1.5px;
  }
  .slot .fill {
    flex: 1;
    margin-left: 6px;
    border-bottom: 2px dotted var(--dot-line);
    height: 10px;
  }

  /* Front: brand side */
  .card-front {
    background: radial-gradient(circle at 45% 35%, #1b1c22 0%, var(--card-black) 70%);
    font-family: "Roboto", sans-serif;
  }
  .dot-field {
    position: absolute;
    right: 0; top: 0;
    width: 230px; height: 100%;
    background: linear-gradient(90deg, rgba(53,199,230,0) 0%, rgba(53,199,230,0.28) 45%, rgba(106,63,199,0.6) 100%);
  }
  .brand {
    position: absolute;
    left: 96px; top: 26px;
    display: flex;
    align-items: center;
    gap: 14px;
  }
  .brand-dot {
    flex: none;
    width: 50px; height: 50px;
    border-radius: 50%;
    background: var(--gold);
    box-shadow: 0 0 14px var(--neon-blue);
  }
  .brand-name {
    font-size: 20px;
    font-weight: 500;
    line-height: 1.2;
    color: var(--gold);
    letter-spacing: 0.4px;
  }
  .doctor {
    position: absolute;
    left: 22px; top: 104px;
    font-size: 15px;
    font-weight: 700;
    color: var(--gold);
  }
  .contacts {
    position: absolute;
    left: 22px; top: 132px;
    list-style: none;
    font-size: 12px;
    color: var(--neon-blue);
  }
  .contacts li {
    display: flex;
    align-items: flex-start;
    gap: 10px;
    margin-bottom: 7px;
    line-height: 1.3;
  }
  .icon {
    flex: none;
    width: 15px; height: 15px;
    border-radius: 50%;
    background: var(--gold);
    display: flex; align-items: center; justify-content: center;
  }
  .icon svg { width: 10px; height: 10px; }
</style>
</head>
<body>

  <section class="card card-back" aria-label="Appointment card, back">
    <div class="faint-mark" aria-hidden="true"></div>
    <h2 class="appointment-title">APPOINTMENT</h2>
    <div class="slots">
      <div class="slot">DATE:<span class="fill"></span></div>
      <div class="slot">TIME:<span class="fill"></span></div>
      <div class="slot">DATE:<span class="fill"></span></div>
      <div class="slot">TIME:<span class="fill"></span></div>
      <div class="slot">DATE:<span class="fill"></span></div>
      <div class="slot">TIME:<span class="fill"></span></div>
      <div class="slot">DATE:<span class="fill"></span></div>
      <div class="slot">TIME:<span class="fill"></span></div>
    </div>
  </section>

  <section class="card card-front" aria-label="Business card, front">
    <div class="dot-field" role="img" aria-label="Decorative field of cyan-to-purple dots fading in from the right edge"></div>
    <div class="brand">
      <span class="brand-dot" aria-hidden="true"></span>
      <span class="brand-name">Lumen<br>Family &amp; Cosmetic Dentistry</span>
    </div>
    <p class="doctor">Lan B. Okafor DMD,PC</p>
    <ul class="contacts">
      <li>
        <span class="icon"><svg viewBox="0 0 10 10"><path d="M2 1 L4 1 L4.6 3 L3.5 3.8 Q4.5 5.8 6.2 6.5 L7 5.4 L9 6 L9 8 Q5 8.5 2.5 5.5 Q1 3.5 2 1Z" fill="#0b0b0d"/></svg></span>
        Ph. 703-555-0187
      </li>
      <li>
        <span class="icon"><svg viewBox="0 0 10 10"><rect x="3" y="1.2" width="4" height="2.6" fill="none" stroke="#0b0b0d" stroke-width="0.8"/><rect x="1.5" y="3.8" width="7" height="3.4" fill="#0b0b0d"/><rect x="3" y="6.4" width="4" height="2.4" fill="#d9ad3c" stroke="#0b0b0d" stroke-width="0.8"/></svg></span>
        Fax 703-5550193
      </li>
      <li>
        <span class="icon"><svg viewBox="0 0 10 10"><circle cx="5" cy="5" r="3.6" fill="none" stroke="#0b0b0d" stroke-width="1"/><path d="M1.4 5 H8.6 M5 1.4 Q3 5 5 8.6 M5 1.4 Q7 5 5 8.6" fill="none" stroke="#0b0b0d" stroke-width="0.8"/></svg></span>
        lumenfacialsmile.com
      </li>
      <li>
        <span class="icon"><svg viewBox="0 0 10 10"><path d="M5 9 Q2 5.5 2 3.8 A3 3 0 0 1 8 3.8 Q8 5.5 5 9Z" fill="#0b0b0d"/><circle cx="5" cy="3.8" r="1.1" fill="#d9ad3c"/></svg></span>
        <span>38412 Brantley Court ,ste.207<br>Cedar Hollow ,VA 20391</span>
      </li>
      <li>
        <span class="icon" aria-hidden="true"></span>
        dentistlan
      </li>
    </ul>
  </section>

</body>
</html>
```